Label design for Kombucha bottles

I'm in the process of making a new brand of Kombucha called Wren Kombucha. Looking for something minimal, but with character.
NOTE: Kombucha is not a beer, it's a fermented flavoured tea which is a healthy alternative to soft drink - and as such doesn't contain any alcohol and is sugar-free.
The label can incorporate "The Quiet Lantern" logo if you so wish (not essential), also came up with a rough idea of a firey barrel idea to get you started, but interested in any other ideas. (On second thoughts disregard this, don't put in quiet lantern logo)
Specifications wise: the label will go on the front of a 330ml beer bottle on an oval-shaped label. Would be good to have examples on a bottle to reference the size of the design. Only for a size guide see the Tallbrook label
Target Market(s)
Hipster crowd
Logo Text
Wren Kombucha
Logo styles of interest
Character Logo
Colors
Designer to choose colors to be used in the design.
Look and feel

```html
<!DOCTYPE html>
<html lang="en">
<head>
<meta charset="utf-8">
<title>Wren Kombucha – Bottle Labels</title>
<link rel="stylesheet" href="https://fonts.googleapis.com/css2?family=Oswald:wght@500;700&display=swap">
<style>
  :root {
    --backdrop: #fce6a8;
    --label-green: #1d7a2c;
    --label-green-deep: #0e5c1f;
    --band-green: #138a2a;
    --gold: #f2d230;
    --gold-soft: #d9b92a;
    --gold-line: #e8c84a;
  }
  html, body {
    margin: 0;
    padding: 0;
    width: 1200px;
    height: 1029px;
    overflow: hidden;
    background: var(--backdrop);
  }
  .label-sheet {
    display: block;
    width: 1200px;
    height: 1029px;
  }
  .brand-small {
    font-family: "Oswald", sans-serif;
    font-weight: 700;
    font-size: 62px;
    fill: var(--gold);
    letter-spacing: 4px;
  }
  .brand-large {
    font-family: "Oswald", sans-serif;
    font-weight: 700;
    font-size: 96px;
    fill: var(--gold);
    letter-spacing: 2px;
  }
  .tagline {
    font-family: "Oswald", sans-serif;
    font-weight: 500;
    font-size: 26px;
    fill: var(--gold);
    letter-spacing: 6px;
  }
  .claim {
    font-family: "Oswald", sans-serif;
    font-weight: 700;
    font-size: 23px;
    fill: var(--gold);
    letter-spacing: 2px;
  }
  .volume {
    font-family: "Oswald", sans-serif;
    font-weight: 700;
    font-size: 30px;
    fill: var(--gold);
  }
</style>
</head>
<body>
<svg class="label-sheet" viewBox="0 0 1200 1029" xmlns="http://www.w3.org/2000/svg">
  <defs>
    <linearGradient id="oval-fill" x1="0" y1="0" x2="1" y2="0">
      <stop offset="0" stop-color="#2f8a3a"/>
      <stop offset="0.45" stop-color="#4d8a55"/>
      <stop offset="1" stop-color="var(--label-green-deep)"/>
    </linearGradient>
    <linearGradient id="character-fill" x1="0" y1="0" x2="1" y2="1">
      <stop offset="0" stop-color="#f6dc3c"/>
      <stop offset="1" stop-color="#d4b020"/>
    </linearGradient>
    <path id="tagline-arc" d="M530 655 Q760 630 990 655"/>
  </defs>

  <!-- Neck label -->
  <g class="neck-label">
    <path d="M120 250 Q250 232 380 250 L380 720 Q250 765 120 720 Z" fill="var(--label-green)"/>
    <path d="M120 268 Q250 250 380 268" fill="none" stroke="var(--gold-line)" stroke-width="3"/>
    <path d="M120 700 Q250 742 380 700" fill="none" stroke="var(--gold-line)" stroke-width="3"/>
    <rect x="160" y="330" width="180" height="320" rx="24" fill="url(#character-fill)" opacity="0.85"
          role="img" aria-label="Character illustration: a walking wanderer carrying a bundle on a stick"/>
  </g>

  <!-- Oval front label -->
  <g class="front-label">
    <ellipse cx="760" cy="515" rx="262" ry="425" fill="var(--label-green)"/>
    <ellipse cx="760" cy="515" rx="246" ry="408" fill="url(#oval-fill)" stroke="var(--gold-line)" stroke-width="4"/>
    <ellipse cx="760" cy="515" rx="234" ry="395" fill="none" stroke="var(--gold-line)" stroke-width="1.5"/>

    <rect x="645" y="170" width="230" height="265" rx="26" fill="url(#character-fill)" opacity="0.85"
          role="img" aria-label="Character illustration: a walking wanderer carrying a bundle on a stick"/>

    <g class="name-band">
      <polygon points="488,468 1032,442 1032,600 488,626" fill="var(--band-green)"/>
      <line x1="488" y1="476" x2="1032" y2="450" stroke="var(--gold-line)" stroke-width="2.5"/>
      <line x1="488" y1="618" x2="1032" y2="592" stroke="var(--gold-line)" stroke-width="2.5"/>
      <text class="brand-small" x="760" y="530" text-anchor="middle">WREN</text>
      <text class="brand-large" x="760" y="605" text-anchor="middle" textLength="470" lengthAdjust="spacingAndGlyphs">KOMBUCHA</text>
    </g>

    <line x1="560" y1="640" x2="960" y2="640" stroke="var(--gold-line)" stroke-width="1.5"/>
    <text class="tagline"><textPath href="#tagline-arc" startOffset="50%" text-anchor="middle">FERMENTED FLAVOURED TEA</textPath></text>

    <text class="claim" x="760" y="800" text-anchor="middle">SUGAR-FREE</text>
    <text class="claim" x="760" y="838" text-anchor="middle">ALCOHOL-FREE</text>
    <text class="volume" x="760" y="910" text-anchor="middle">330ml</text>
  </g>
</svg>
</body>
</html>
```